BrivoLane Ute.

I want the full logo on one side. And the other side the card if right Ralf the logo the left half orange like the car in the logo color with Danielle R Morrow
Founder and CEO
Email symbol then dmorrow@brivolaneute.com
Www symbol. Then Brivolaneute.com
Phone symbol then 413-926-BRIV
The very bottom would like Brivo Lane Ute is a division of Harmond Vistas. LLC

```html
<!DOCTYPE html>
<html lang="en">
<head>
<meta charset="utf-8">
<title>Brivo Lane Ute – Business Card</title>
<link rel="stylesheet" href="https://fonts.googleapis.com/css2?family=Open+Sans:wght@400;600;700&family=Gelasio:wght@400&display=swap">
<style>
  :root {
    --orange: #e98d27;
    --orange-soft: #f3b56b;
    --teal: #bfe6e0;
    --ink: #1f1d1c;
    --page: #ffffff;
    --card-front: #ffffff;
    --card-back: #f2f2f2;
    --edge: #d6d6d6;
    --shadow: rgba(0, 0, 0, 0.55);
  }
  * { box-sizing: border-box; margin: 0; padding: 0; }
  html, body {
    width: 1200px; height: 974px; overflow: hidden;
    background: var(--page);
  }
  .canvas { position: relative; width: 1200px; height: 974px; }

  .card {
    position: absolute;
    left: 338px; width: 561px;
    border: 1px solid var(--edge);
    box-shadow: -22px 22px 18px var(--shadow);
    overflow: hidden;
  }
  .card--front { top: 138px; height: 343px; background: var(--card-front); }
  .card--back { top: 543px; height: 336px; background: var(--card-back); }

  .front-illustration {
    position: absolute; left: 0; top: 107px; width: 213px; height: 133px;
    background: linear-gradient(180deg, #fff4dc 0%, var(--orange-soft) 55%, #e7c9a5 100%);
    border-radius: 0 6px 6px 0;
  }

  .person { position: absolute; right: 22px; top: 42px; text-align: right; }
  .person__name {
    font-family: "Open Sans", sans-serif; font-weight: 600;
    font-size: 37px; line-height: 1; color: var(--orange); letter-spacing: -0.3px;
  }
  .person__title {
    margin-top: 10px;
    font-family: "Open Sans", sans-serif; font-weight: 400;
    font-size: 19px; color: var(--orange); letter-spacing: 1px;
  }

  .contact { position: absolute; left: 277px; top: 169px; list-style: none; }
  .contact__item {
    display: flex; align-items: center; gap: 7px; height: 26px;
    font-family: "Gelasio", serif; font-size: 14px; color: var(--orange);
  }
  .contact__icon { width: 18px; height: 18px; flex: none; }

  .division-band {
    position: absolute; left: 0; right: 0; top: 278px; height: 32px;
    background: var(--orange);
    display: flex; align-items: center; justify-content: center;
    font-family: "Gelasio", serif; font-size: 14px; color: #fff; letter-spacing: 0.3px;
  }

  .logo-illustration {
    position: absolute; left: 98px; top: 51px; width: 365px; height: 131px;
    background: linear-gradient(180deg, #fff2d6 0%, var(--orange-soft) 45%, var(--orange) 100%);
    border-radius: 8px;
  }
  .brand-name {
    position: absolute; left: 0; right: 0; top: 184px; text-align: center;
    font-family: "Open Sans", sans-serif; font-weight: 700;
    font-size: 40px; color: var(--ink); letter-spacing: 1px;
  }
</style>
</head>
<body>
<main class="canvas">

  <section class="card card--front" aria-label="Card front">
    <div class="front-illustration" role="img" aria-label="Illustration of an orange vintage woody wagon with a surfboard and wine bottles beside a beach fence"></div>

    <div class="person">
      <h1 class="person__name">Danielle R Morrow</h1>
      <p class="person__title">Founder and CEO</p>
    </div>

    <ul class="contact">
      <li class="contact__item">
        <svg class="contact__icon" viewBox="0 0 20 20" aria-hidden="true">
          <rect x="1" y="4" width="18" height="12" fill="var(--orange)"/>
          <path d="M1 4 L10 11 L19 4" fill="none" stroke="#fff" stroke-width="1.6"/>
        </svg>
        dmorrow@brivolaneute.com
      </li>
      <li class="contact__item">
        <svg class="contact__icon" viewBox="0 0 20 20" aria-hidden="true">
          <path d="M5 2 L8 6 L6.5 8 Q8.5 12 12 13.5 L14 12 L18 15 L16 18 Q9 18.5 4.5 13 Q1 8 3 3 Z" fill="none" stroke="var(--orange)" stroke-width="1.6" stroke-linejoin="round"/>
          <path d="M12 3 Q16 4 17 8 M12 6 Q14 6.5 14.5 8.5" fill="none" stroke="var(--orange)" stroke-width="1.4"/>
        </svg>
        413-926-BRIV
      </li>
      <li class="contact__item">
        <svg class="contact__icon" viewBox="0 0 20 20" aria-hidden="true">
          <g fill="none" stroke="var(--orange)" stroke-width="1.4">
            <circle cx="10" cy="10" r="8"/>
            <ellipse cx="10" cy="10" rx="3.5" ry="8"/>
            <path d="M2 10 H18 M3.5 6 H16.5 M3.5 14 H16.5"/>
          </g>
        </svg>
        Brivolaneute.com
      </li>
    </ul>

    <div class="division-band">Brivo Lane Ute is a division of Harmond Vistas. LLC</div>
  </section>

  <section class="card card--back" aria-label="Card back">
    <div class="logo-illustration" role="img" aria-label="Illustration of an orange vintage woody wagon with a surfboard, wine bottles and beach fences under a rising sun"></div>
    <p class="brand-name">BRIVO LANE UTE</p>
  </section>

</main>
</body>
</html>
```